Lantern Hill Publicity is a new boutique Press Office with a small roster of well-chosen clients across an array of disciplines; from Art and Technology to Restaurants and Fashion. Based in Greenpoint Brooklyn, Lantern Hill Publicity achieves outstanding results through hard work, tenacity, efficiency and a sense of humor. We need a simple, versatile and classic design. We would like each side of the card to be white text on a black background.

Boutique

```html
<!DOCTYPE html>
<html lang="en">
<head>
<meta charset="utf-8">
<title>Lantern Hill Publicity — Business Card</title>
<link rel="stylesheet" href="https://fonts.googleapis.com/css2?family=Source+Sans+3:wght@400;600;700&display=swap">
<style>
  :root {
    --page: #e4e2de;
    --card-black: #0e0e0f;
    --card-sheen: #2a2a2c;
    --ink-white: #ffffff;
    --ink-soft: #d9d9d9;
    --wave-light: #f2f2f2;
    --wave-mid: #a9a9ab;
  }
  * { box-sizing: border-box; margin: 0; padding: 0; }
  html, body { width: 1200px; height: 843px; overflow: hidden; }
  body {
    background: var(--page);
    font-family: "Source Sans 3", "Helvetica Neue", Arial, sans-serif;
    display: flex;
    align-items: center;
    justify-content: center;
    gap: 40px;
  }
  .card {
    position: relative;
    width: 540px;
    height: 308px;
    border-radius: 18px;
    overflow: hidden;
    background: linear-gradient(160deg, var(--card-sheen) 0%, var(--card-black) 45%, var(--card-black) 100%);
    color: var(--ink-white);
    box-shadow: 0 10px 28px rgba(0,0,0,0.25);
  }
  .wordmark {
    text-transform: uppercase;
    font-weight: 400;
    color: var(--ink-white);
    text-align: center;
    line-height: 1.1;
  }
  .wordmark .name { display: block; letter-spacing: 0.14em; }
  .wordmark .sub { display: block; letter-spacing: 0.5em; }
  .card-front .wordmark {
    position: absolute;
    left: 0; right: 0; top: 50%;
    transform: translateY(-50%);
  }
  .card-front .wordmark .name { font-size: 30px; }
  .card-front .wordmark .sub { font-size: 12px; margin-top: 6px; }

  .card-back .person { position: absolute; left: 34px; top: 52px; }
  .person-name { font-size: 19px; font-weight: 600; letter-spacing: 0.03em; }
  .person-role { font-size: 13px; color: var(--ink-soft); margin-top: 2px; }
  .card-back .wordmark { position: absolute; right: 34px; top: 48px; text-align: right; }
  .card-back .wordmark .name { font-size: 18px; }
  .card-back .wordmark .sub { font-size: 9px; margin-top: 4px; }

  .contact {
    position: absolute;
    right: 34px;
    bottom: 56px;
    text-align: right;
    font-size: 13px;
    line-height: 1.65;
    color: var(--ink-white);
  }
  .contact b { font-weight: 700; }
  .wave { position: absolute; left: 0; bottom: 0; width: 100%; height: 70px; }
</style>
</head>
<body>
  <section class="card card-front" aria-label="Card front">
    <div class="wordmark">
      <span class="name">Lantern Hill</span>
      <span class="sub">Publicity</span>
    </div>
  </section>

  <section class="card card-back" aria-label="Card back">
    <div class="person">
      <p class="person-name">DANIEL REYES</p>
      <p class="person-role">CEO/Founder</p>
    </div>
    <div class="wordmark">
      <span class="name">Lantern Hill</span>
      <span class="sub">Publicity</span>
    </div>
    <div class="contact">
      <p>214 Franklin Street, Brooklyn, New York 11222</p>
      <p><b>Phone:</b> 718 555 0142 &nbsp;<b>Mobile:</b> 917 555 0187 &nbsp;<b>Fax:</b> 718 555 0199</p>
      <p><b>Email:</b> hello@lanternhillpr.com &nbsp;<b>Web:</b> www.lanternhillpr.com</p>
    </div>
    <svg class="wave" viewBox="0 0 540 70" preserveAspectRatio="none" aria-hidden="true">
      <path d="M0 8 C 60 30, 140 58, 260 64 C 360 68, 460 66, 540 70 L 0 70 Z" fill="var(--wave-mid)"/>
      <path d="M0 26 C 70 46, 160 64, 280 68 C 380 70, 470 70, 540 70 L 0 70 Z" fill="var(--wave-light)"/>
    </svg>
  </section>
</body>
</html>
```